Design my Display Ad! Product for Muscle Cramps -- Need Your Talent!

I need the PSD of a square display ad to be the design concept for other ad formats. The product is for leg and muscle cramps. The ad needs to encourage clicks, not simply impressions. Image should contain legs.

Visit www.legsoothewell.com for a better idea of the product.

Target Market(s)

People age 55+ with leg cramps

Industry/Entity Type

Health And Wellness

Font styles to use
Sans Serif

Colors

Designer to choose colors to be used in the design.

Requirements
Must have
• One version with the text:
• The Real Cause of Leg Cramps
• Discover the Secret
• The other version with the text:
• Leg Cramps at Night
• Discover the Real Cause
• An image focused on legs.
• Attractive presentation -- this is a premium organic brand.
• Visit www.legsoothewell.com for a better understanding of the product

```html
<!DOCTYPE html>
<html lang="en">
<head>
<meta charset="utf-8">
<title>Leg Cramps at Night — Display Ad</title>
<link rel="stylesheet" href="https://fonts.googleapis.com/css2?family=Archivo:wght@300;400;700&display=swap">
<style>
  :root {
    --mint-bg: #d4fcb4;
    --panel: #ffffff;
    --green-dark: #5aab2c;
    --green: #7dbe50;
    --cta: #7dbe50;
    --cta-text: #ffffff;
    --url-grey: #9a9a9a;
  }
  html, body {
    margin: 0;
    padding: 0;
    width: 1200px;
    height: 1200px;
    overflow: hidden;
    background: var(--mint-bg);
  }
  .ad {
    position: relative;
    width: 1200px;
    height: 1200px;
    background: var(--mint-bg);
    font-family: "Archivo", Arial, sans-serif;
  }
  .panel {
    position: absolute;
    left: 150px;
    top: 150px;
    width: 900px;
    height: 450px;
    background: var(--panel);
  }
  .photo {
    position: absolute;
    left: 150px;
    top: 600px;
    width: 900px;
    height: 450px;
    background:
      radial-gradient(ellipse at 30% 30%, #fffbe0 0%, #f4f0a8 25%, rgba(220,220,120,0) 60%),
      linear-gradient(180deg, #d9d48a 0%, #b7b860 45%, #6a7a2e 75%, #3f5a1e 100%);
  }
  .headline {
    position: absolute;
    margin: 0;
    font-weight: 700;
    line-height: 1;
    letter-spacing: 0;
  }
  .headline-top {
    left: 263px;
    top: 282px;
    font-size: 74px;
    color: var(--green-dark);
  }
  .headline-bottom {
    left: 562px;
    top: 358px;
    font-size: 74px;
    color: var(--green);
  }
  .headline-bottom .light { font-weight: 300; }
  .cta-frame {
    position: absolute;
    left: 244px;
    top: 485px;
    width: 712px;
    height: 222px;
    border: 1px solid var(--green-dark);
    box-sizing: border-box;
  }
  .cta {
    position: absolute;
    left: 268px;
    top: 511px;
    width: 663px;
    height: 170px;
    background: var(--cta);
    color: var(--cta-text);
    display: flex;
    align-items: center;
    justify-content: center;
    font-weight: 700;
    font-size: 40px;
    letter-spacing: 0;
  }
  .url {
    position: absolute;
    left: 0;
    top: 1062px;
    width: 1200px;
    text-align: center;
    font-size: 34px;
    letter-spacing: 8px;
    color: var(--url-grey);
    text-transform: uppercase;
  }
</style>
</head>
<body>
  <div class="ad">
    <div class="panel"></div>
    <div class="photo" role="img" aria-label="Close-up of legs in running shoes walking on a mossy rock in warm backlit sunlight"></div>
    <h1 class="headline headline-top">LEG CRAMPS</h1>
    <p class="headline headline-bottom"><span class="light">AT</span> NIGHT</p>
    <div class="cta-frame"></div>
    <div class="cta">DISCOVER THE REAL CAUSE</div>
    <div class="url">www.legsoothewell.com</div>
  </div>
</body>
</html>
```